We need a fresh, new church business card!!

We need a church business card with basic info to hand out as invites. We are looking for something clean that communicates our basic information clearly.

We are open to square or rectangle card sizes.

General Public

Religious

The attached logo is the only one that I have available. We'd like to see options with with text of the logo lighter and on a dark background as well as options with white/light backgrounds.

Also, we'd like to see option with rounded corners.

• Address - 2718 Maple Row, Alderton, OH 44102
• Website - brookvane.example
• Phone - 815-555-0163
• Service times -
• Sunday - 10am Sunday School
• - 11am Family Worship
• - 6pm Night of Prayer
• Wednesday - 7:30pm Adult Bible Study
• Classes for all ages

```html
<!DOCTYPE html>
<html lang="en">
<head>
<meta charset="utf-8">
<title>Brookvane Pentecostal Church — Business Card</title>
<link rel="stylesheet" href="https://fonts.googleapis.com/css2?family=Montserrat:wght@500&family=PT+Sans:wght@400;700&display=swap">
<style>
  :root {
    --teal: #5693a5;
    --teal-dark: #4a8396;
    --grey: #6f6f71;
    --grey-text: #6a6a6c;
    --white: #ffffff;
    --page: #ecedee;
  }
  * { box-sizing: border-box; margin: 0; padding: 0; }
  html, body { width: 1200px; height: 1200px; overflow: hidden; background: var(--page); }
  body { position: relative; font-family: "PT Sans", Arial, sans-serif; }

  .card {
    position: absolute;
    left: 150px;
    width: 900px;
    height: 514px;
    overflow: hidden;
    box-shadow: 0 6px 24px rgba(0,0,0,0.14);
  }
  .card--front { top: 60px; background: var(--white); }
  .card--back  { top: 626px; background: var(--teal); color: var(--white); }

  .church-name {
    font-family: "Montserrat", Arial, sans-serif;
    font-weight: 500;
    line-height: 1;
  }
  .church-name__main { display: block; font-size: 58px; letter-spacing: 1px; text-transform: uppercase; }
  .church-name__sub  { display: block; font-size: 19px; letter-spacing: 7px; text-transform: uppercase; margin-top: 6px; }

  /* Front */
  .wave { position: absolute; left: 0; top: 0; width: 900px; height: 514px; }

  .front-brand {
    position: absolute; left: 70px; top: 50px;
    display: flex; align-items: center; gap: 22px;
    color: var(--grey);
  }
  .brand-dot { width: 74px; height: 74px; border-radius: 50%; background: var(--teal); flex: none; }

  .person { position: absolute; left: 70px; top: 188px; }
  .person__name { color: var(--teal); font-weight: 700; font-size: 34px; line-height: 1.1; }
  .person__role { color: var(--grey-text); font-size: 23px; margin-top: 2px; }

  .divider { position: absolute; left: 372px; top: 190px; width: 2px; height: 186px; background: var(--teal); }

  .contact { position: absolute; left: 400px; top: 226px; color: var(--grey-text); font-size: 23px; line-height: 1.38; list-style: none; }
  .contact__line { display: flex; align-items: center; gap: 10px; }
  .contact__icon { width: 20px; height: 20px; flex: none; }

  /* Back */
  .back-mark {
    position: absolute; left: -120px; top: -110px;
    width: 420px; height: 420px; border-radius: 50%;
    background: var(--teal-dark); opacity: 0.55;
  }
  .back-brand { position: absolute; left: 0; right: 0; top: 96px; text-align: center; }

  .times { position: absolute; left: 0; right: 0; top: 250px; display: flex; justify-content: center; gap: 40px; }
  .times__box {
    width: 330px; padding: 18px 16px;
    border: 2px solid var(--white);
    text-align: center; font-size: 22px; line-height: 1.3;
  }
  .times__day { font-weight: 700; font-size: 23px; }
</style>
</head>
<body>

<section class="card card--front">
  <svg class="wave" viewBox="0 0 900 514" aria-hidden="true">
    <path d="M0,330 Q300,440 570,466 Q770,482 900,446 L900,514 L0,514 Z" fill="var(--teal)"/>
    <path d="M0,292 Q290,405 590,464 Q280,420 0,316 Z" fill="var(--grey)"/>
  </svg>

  <div class="front-brand">
    <span class="brand-dot"></span>
    <div class="church-name">
      <span class="church-name__main">Brookvane</span>
      <span class="church-name__sub">Pentecostal Church</span>
    </div>
  </div>

  <div class="person">
    <p class="person__name">Daniel Reyes</p>
    <p class="person__role">Managing Partner</p>
  </div>

  <div class="divider"></div>

  <ul class="contact">
    <li>2718 Maple Row,</li>
    <li>Alderton, OH 44102</li>
    <li class="contact__line">
      <svg class="contact__icon" viewBox="0 0 20 20" aria-hidden="true">
        <path d="M3 4 Q10 0 17 4 L15 7 Q10 5 5 7 Z" fill="var(--teal)"/>
        <rect x="5" y="9" width="10" height="8" rx="2" fill="var(--teal)"/>
      </svg>
      815-555-0163
    </li>
    <li class="contact__line">
      <svg class="contact__icon" viewBox="0 0 20 20" aria-hidden="true">
        <circle cx="10" cy="10" r="9" fill="var(--teal)"/>
        <ellipse cx="10" cy="10" rx="4" ry="9" fill="none" stroke="var(--white)" stroke-width="1.2"/>
        <line x1="1" y1="10" x2="19" y2="10" stroke="var(--white)" stroke-width="1.2"/>
      </svg>
      brookvane.example
    </li>
  </ul>
</section>

<section class="card card--back">
  <div class="back-mark"></div>

  <div class="back-brand church-name">
    <span class="church-name__main">Brookvane</span>
    <span class="church-name__sub">Pentecostal Church</span>
  </div>

  <div class="times">
    <div class="times__box">
      <p class="times__day">Sunday</p>
      <p>10am Sunday School</p>
      <p>11am Family Worship</p>
      <p>6pm Night of Prayer</p>
    </div>
    <div class="times__box">
      <p class="times__day">Wednesday</p>
      <p>7:30pm Adult Bible Study</p>
      <p>Classes for all ages</p>
    </div>
  </div>
</section>

</body>
</html>
```